Ferris Contracting LLC Business Card Design

I am looking for a creative and unique business card design. We are a commercial construction general contractor. With the name "FERRIS" Contracting, I am hoping to see some neat designs that correlate with the name.

```html
<!DOCTYPE html>
<html lang="en">
<head>
<meta charset="utf-8">
<title>Ferris Contracting – Business Card</title>
<link rel="stylesheet" href="https://fonts.googleapis.com/css2?family=Inter:wght@500;700;800&display=swap">
<style>
  :root {
    --stage: #3d3835;
    --card-dark: #1c1c1e;
    --brand-blue: #0ba1dd;
    --blue-deep: #0079c1;
    --blue-light: #00a8e0;
    --divider: #9a9a9a;
    --ink: #4a4a4a;
    --paper: #ffffff;
  }
  * { margin: 0; padding: 0; box-sizing: border-box; }
  html, body {
    width: 1200px; height: 1200px; overflow: hidden;
    background: var(--stage);
    font-family: "Inter", Arial, sans-serif;
  }
  .card {
    position: absolute; left: 179px; width: 861px; height: 495px;
    box-shadow: 0 6px 18px rgba(0,0,0,.35);
    overflow: hidden;
  }
  .card--front { top: 84px; background: var(--card-dark); }
  .card--back { top: 622px; background: var(--paper); }

  .wordmark {
    position: absolute; display: flex; align-items: center; gap: 16px;
    font-weight: 800; letter-spacing: 3px; white-space: nowrap;
  }
  .wordmark__dot { width: 22px; height: 22px; border-radius: 50%; background: currentColor; }
  .card--front .wordmark {
    left: 50%; top: 50%; transform: translate(-50%, -50%);
    color: var(--brand-blue); font-size: 50px;
  }

  .brand-panel {
    position: absolute; left: 0; top: 0; width: 416px; height: 100%;
    background: linear-gradient(90deg, var(--blue-deep) 0%, var(--blue-light) 45%, var(--blue-light) 60%, var(--blue-deep) 100%);
    border-right: 4px solid var(--divider);
  }
  .brand-panel .wordmark {
    left: 50%; top: 50%; transform: translate(-50%, -50%);
    color: var(--paper); font-size: 27px; gap: 10px; letter-spacing: 2px;
  }
  .brand-panel .wordmark__dot { width: 14px; height: 14px; }

  .details { position: absolute; left: 443px; top: 0; right: 0; bottom: 0; color: var(--ink); }
  .details__name {
    position: absolute; top: 42px; font-size: 28px; font-weight: 700;
    color: var(--brand-blue); letter-spacing: .5px;
  }
  .details__role { position: absolute; top: 88px; font-size: 22px; font-weight: 500; letter-spacing: 2px; }
  .contact { position: absolute; top: 240px; list-style: none; }
  .contact li {
    display: flex; align-items: center; gap: 12px; height: 28.5px;
    font-size: 22px; font-weight: 500; letter-spacing: 3px;
  }
  .contact svg { width: 22px; height: 22px; flex: none; fill: var(--brand-blue); }
  .contact .accent { color: var(--brand-blue); }
  .address { position: absolute; top: 384px; font-size: 22px; font-weight: 500; letter-spacing: 3px; line-height: 29px; font-style: normal; }
</style>
</head>
<body>
  <section class="card card--front">
    <div class="wordmark"><span class="wordmark__dot"></span>FERRIS CONTRACTING</div>
  </section>

  <section class="card card--back">
    <div class="brand-panel">
      <div class="wordmark"><span class="wordmark__dot"></span>FERRIS CONTRACTING</div>
    </div>
    <div class="details">
      <h1 class="details__name">Name Surename</h1>
      <p class="details__role">Director</p>
      <ul class="contact">
        <li>
          <svg viewBox="0 0 24 24" aria-hidden="true"><path d="M6.6 10.8a15.1 15.1 0 0 0 6.6 6.6l2.2-2.2c.3-.3.7-.4 1-.2 1.1.4 2.3.6 3.6.6.6 0 1 .4 1 1V20c0 .6-.4 1-1 1A17 17 0 0 1 3 4c0-.6.4-1 1-1h3.5c.6 0 1 .4 1 1 0 1.3.2 2.5.6 3.6.1.3 0 .7-.2 1z"/></svg>
          0400 127 986
        </li>
        <li>
          <svg viewBox="0 0 24 24" aria-hidden="true"><path d="M2 5h20v14H2zm2 2v.4l8 5 8-5V7zm0 2.8V17h16V9.8l-8 5z"/></svg>
          email@website.com
        </li>
        <li>
          <svg viewBox="0 0 24 24" aria-hidden="true"><path d="M12 2a10 10 0 1 0 0 20 10 10 0 0 0 0-20zm6.9 6h-2.9a15.7 15.7 0 0 0-1.4-3.6A8 8 0 0 1 18.9 8zM12 4c.8 1.2 1.5 2.5 1.9 4h-3.8c.4-1.4 1.1-2.8 1.9-4zM4.3 14a8.2 8.2 0 0 1 0-4h3.4a16 16 0 0 0 0 4zm.8 2h2.9c.3 1.3.8 2.5 1.4 3.6A8 8 0 0 1 5.1 16zM8 8H5.1a8 8 0 0 1 4.3-3.6C8.8 5.5 8.3 6.7 8 8zm4 12c-.8-1.2-1.5-2.5-1.9-4h3.8c-.4 1.4-1.1 2.8-1.9 4zm2.3-6H9.7a14.6 14.6 0 0 1 0-4h4.6a14.6 14.6 0 0 1 0 4zm.3 5.6c.6-1.1 1.1-2.3 1.4-3.6h2.9a8 8 0 0 1-4.3 3.6zm1.7-5.6a16 16 0 0 0 0-4h3.4a8.2 8.2 0 0 1 0 4z"/></svg>
          <span>www.<span class="accent">website</span>.com</span>
        </li>
      </ul>
      <address class="address">Anywhere St.<br>Any City, ST 12345</address>
    </div>
  </section>
</body>
</html>
```